Larkspur Ridge Management - Business Cards

I need business cards. My current logo was designed by a designer at this site and I very much like and am happy with the results. I would like a business card that is trendy, unique, current yet professional. I deal with high net worth clients daily

Target Market(s)

Out of state investors looking to get into the rental market in Ohio

Industry/Entity Type

Property Management, Consulting

Contact Information for Business Card

Name, Title (Chief Financial Officer) office phone number (555) 817-3094 website address larkridgemgmt.example

Font styles to use
Sans Serif

Colors
0054AA
0677BA
7BADD7
CADEEF
E8F1F8
0094D4
00A9DD
6FCCEA
C7EBF8
E9F6FB
00AB8E
00BBA5
67D7C9
C6EFE9
E9F9F6

```html
<!DOCTYPE html>
<html lang="en">
<head>
<meta charset="utf-8">
<title>Larkspur Ridge Management – Business Cards</title>
<link rel="stylesheet" href="https://fonts.googleapis.com/css2?family=Montserrat:wght@700;800&family=Lato:wght@400;700&display=swap">
<style>
  :root {
    --backdrop: #3a3b3f;
    --brand-blue: #0054AA;
    --mid-blue: #0677BA;
    --sky: #0094D4;
    --teal: #00AB8E;
    --teal-bright: #00BBA5;
    --paper: #F7FAFC;
    --stripe: #CADEEF;
    --ink: #0054AA;
    --body-ink: #2c3e55;
    --white: #ffffff;
  }
  * { margin: 0; padding: 0; box-sizing: border-box; }
  html, body { width: 1200px; height: 682px; overflow: hidden; }
  body {
    background: var(--backdrop);
    position: relative;
    font-family: "Lato", sans-serif;
  }
  .card {
    position: absolute;
    width: 540px;
    height: 309px;
    overflow: hidden;
  }

  /* Back of card */
  .card-back {
    left: 50px;
    top: 80px;
    background: var(--brand-blue);
    display: flex;
    align-items: center;
    justify-content: center;
  }
  .brand-name {
    font-family: "Montserrat", sans-serif;
    font-weight: 800;
    text-transform: uppercase;
    text-align: center;
    line-height: 1.15;
  }
  .card-back .brand-name {
    color: var(--white);
    font-size: 34px;
    letter-spacing: 1px;
  }

  /* Front of card */
  .card-front {
    left: 610px;
    top: 290px;
    background: var(--paper);
  }
  .accent-rule {
    position: absolute;
    left: 58px;
    top: 52px;
    width: 2px;
    height: 196px;
    background: var(--teal);
  }
  .person-name {
    position: absolute;
    left: 84px;
    top: 50px;
    font-family: "Montserrat", sans-serif;
    font-weight: 800;
    font-size: 23px;
    color: var(--ink);
    letter-spacing: 0.3px;
  }
  .person-title {
    position: absolute;
    left: 86px;
    top: 84px;
    font-family: "Montserrat", sans-serif;
    font-weight: 700;
    font-size: 13px;
    color: var(--teal);
    letter-spacing: 0.4px;
  }
  .contact-list {
    position: absolute;
    left: 84px;
    top: 130px;
    list-style: none;
  }
  .contact-item {
    display: flex;
    align-items: flex-start;
    gap: 10px;
    font-size: 12.5px;
    color: var(--body-ink);
    height: 30px;
    line-height: 1.3;
  }
  .contact-item svg { flex: none; width: 18px; height: 18px; margin-top: -1px; }
  .card-front .brand-block {
    position: absolute;
    right: 22px;
    top: 82px;
    width: 200px;
    display: flex;
    flex-direction: column;
    align-items: center;
    gap: 10px;
  }
  .brand-dot {
    width: 16px;
    height: 16px;
    border-radius: 50%;
    background: var(--teal);
  }
  .card-front .brand-name {
    color: var(--brand-blue);
    font-size: 17px;
  }
  .footer-band {
    position: absolute;
    left: 0;
    bottom: 0;
    width: 400px;
    height: 36px;
    background: var(--brand-blue);
  }
  .footer-deco {
    position: absolute;
    right: 0;
    bottom: 0;
  }
</style>
</head>
<body>

  <section class="card card-back" aria-label="Card back">
    <p class="brand-name">Larkspur Ridge<br>Management</p>
  </section>

  <section class="card card-front" aria-label="Card front">
    <div class="accent-rule"></div>
    <h1 class="person-name">MARCUS ELLERY</h1>
    <p class="person-title">CHIEF FINANCIAL OFFICER</p>

    <ul class="contact-list">
      <li class="contact-item">
        <svg viewBox="0 0 18 18" aria-hidden="true"><circle cx="9" cy="9" r="9" fill="#00AB8E"/><path d="M6.2 4.8l1.6 1.9-.8 1.2c.6 1.2 1.6 2.2 2.8 2.8l1.2-.8 1.9 1.6-.9 1.5c-3.6-.4-6.7-3.5-7.1-7.1z" fill="#fff"/></svg>
        <span>(555) 817-3094</span>
      </li>
      <li class="contact-item">
        <svg viewBox="0 0 18 18" aria-hidden="true"><circle cx="9" cy="9" r="9" fill="#00AB8E"/><rect x="4.5" y="6" width="9" height="6.5" fill="none" stroke="#fff" stroke-width="1"/><path d="M4.5 6l4.5 3.8L13.5 6" fill="none" stroke="#fff" stroke-width="1"/></svg>
        <span>marcus@larkridgemgmt.example</span>
      </li>
      <li class="contact-item">
        <svg viewBox="0 0 18 18" aria-hidden="true"><circle cx="9" cy="9" r="9" fill="#00AB8E"/><circle cx="9" cy="9" r="4.8" fill="none" stroke="#fff" stroke-width="1"/><ellipse cx="9" cy="9" rx="2" ry="4.8" fill="none" stroke="#fff" stroke-width="1"/><path d="M4.2 9h9.6" stroke="#fff" stroke-width="1"/></svg>
        <span>www.larkridgemgmt.example</span>
      </li>
      <li class="contact-item">
        <svg viewBox="0 0 18 18" aria-hidden="true"><path d="M9 1.5a5.5 5.5 0 0 0-5.5 5.5c0 4 5.5 10 5.5 10s5.5-6 5.5-10A5.5 5.5 0 0 0 9 1.5z" fill="#00AB8E"/><circle cx="9" cy="7" r="2" fill="#fff"/></svg>
        <span>4870 Meadowgate Drive, Suite 310<br>Dayton, OH 45402</span>
      </li>
    </ul>

    <div class="brand-block">
      <span class="brand-dot"></span>
      <p class="brand-name">Larkspur Ridge<br>Management</p>
    </div>

    <div class="footer-band"></div>
    <svg class="footer-deco" width="200" height="120" viewBox="0 0 200 120" aria-hidden="true">
      <polygon points="60,84 0,84 0,120 60,120" fill="#0054AA"/>
      <polygon points="60,84 110,120 60,120" fill="#00A9DD"/>
      <polygon points="150,120 200,40 200,58 162,120" fill="#CADEEF"/>
      <polygon points="176,120 200,82 200,100 188,120" fill="#CADEEF"/>
    </svg>
  </section>

</body>
</html>
```